Copper Meadow Dental Lab - Presentation Folder Design

1. We are a dental lab providing a full range of dental products to restore and enhance the natural beauty of the patients’ smiles. We provide fixed restorations (Full-Contour Solid Zirconia, KRT o.lumo, Dune Prime, Full Cast, PFM, Temporary Crowns, Diagnostic Wax-Ups and Study Models), implant restorations (Single and Multi Tooth Restorations, Zirconia Prosthesis, Full Arch Hybrid Prosthesis), and
removable restorations (Dentures and Partials, PolyBend, Kernalite).
2. The target market are dentists, oral surgeons, implant manufacturers, and etc. We are not targeting patients.
3. Design specifics - no specifics, but I have provided our logo for reference if needed

Target Market(s)

Dentists, Oral Surgeons, implant manufacturers

Industry/Entity Type

Dental

Requirements
Must have
• Name - Copper Meadow Dental Lab, address - 4126 Orchard Ln, Suite 310, Annandale, VA 22003, office number - 703-555-0142, fax number - 703-555-0143, email - info@cmdentalworks.example

```html
<!DOCTYPE html>
<html lang="en">
<head>
<meta charset="utf-8">
<title>Copper Meadow Dental Lab – Presentation Folder</title>
<link href="https://fonts.googleapis.com/css2?family=Open+Sans:wght@400;600;700&family=Montserrat:wght@300;400&display=swap" rel="stylesheet">
<style>
  :root {
    --page-bg: #eceef1;
    --navy: #1b2f8a;
    --royal: #2c49b8;
    --deep: #0b1f66;
    --text-blue: #2a3fa0;
    --grey-text: #4a4f5c;
    --white: #ffffff;
  }
  * { margin: 0; padding: 0; box-sizing: border-box; }
  html, body { width: 849px; height: 1200px; overflow: hidden; }
  body {
    background: var(--page-bg);
    font-family: "Open Sans", Arial, sans-serif;
    position: relative;
  }
  .folder-spread {
    position: absolute;
    left: 0; top: 300px;
    width: 849px; height: 600px;
    display: flex;
    box-shadow: 0 6px 22px rgba(0,0,0,0.18);
  }
  .panel { position: relative; width: 424.5px; height: 600px; overflow: hidden; }

  /* Back panel */
  .panel--back { background: var(--white); }
  .back-photo {
    position: absolute; left: 0; top: 0; width: 100%; height: 210px;
    background: linear-gradient(180deg, rgba(150,155,165,0.55) 0%, rgba(200,203,210,0.35) 55%, rgba(255,255,255,0) 100%),
                linear-gradient(90deg, #b9bcc4 0%, #e3e5e9 60%, #f4f5f7 100%);
  }
  .brand-name {
    position: absolute; left: 0; width: 100%;
    text-align: center;
    font-family: "Open Sans", Arial, sans-serif;
    font-weight: 700;
    color: var(--navy);
    text-transform: uppercase;
    line-height: 1.1;
  }
  .brand-name--main { top: 122px; font-size: 21px; letter-spacing: 0.5px; }
  .brand-name--small { top: 330px; font-size: 12px; letter-spacing: 0.3px; }
  .services-text {
    position: absolute; left: 74px; top: 228px; width: 280px;
    font-size: 7.2px; line-height: 1.45;
    color: var(--text-blue); font-weight: 600;
  }
  .contact-block {
    position: absolute; left: 0; top: 378px; width: 100%;
    text-align: center; color: var(--grey-text);
    font-size: 6.6px; line-height: 1.55;
  }
  .contact-block .contact-name { font-weight: 700; color: var(--navy); }
  .contact-block .gap { height: 7px; }
  .contact-block .web { color: var(--navy); font-weight: 600; }

  /* Front panel */
  .panel--front {
    background: linear-gradient(180deg, var(--royal) 0%, var(--navy) 40%, var(--deep) 100%);
  }
  .front-photo {
    position: absolute; left: 0; top: 150px; width: 100%; height: 380px;
    background: radial-gradient(ellipse at 35% 45%, rgba(170,200,255,0.55) 0%, rgba(60,100,200,0.35) 40%, rgba(10,30,100,0) 75%),
                linear-gradient(180deg, rgba(30,60,170,0.2), rgba(8,25,90,0.6));
  }
  .tagline {
    position: absolute; left: 0; top: 50px; width: 100%;
    text-align: center; color: var(--white);
    font-size: 7.5px; font-weight: 600; letter-spacing: 0.2px;
  }
  .headline {
    position: absolute; left: 0; top: 72px; width: 100%;
    text-align: center; color: var(--white);
    font-family: "Montserrat", Arial, sans-serif;
    font-weight: 300; font-size: 40px; letter-spacing: 9px;
  }
  .front-web {
    position: absolute; left: 0; bottom: 34px; width: 100%;
    text-align: center; color: var(--white);
    font-size: 6.5px; letter-spacing: 2.5px;
  }
</style>
</head>
<body>
  <div class="folder-spread">
    <section class="panel panel--back">
      <div class="back-photo" role="img" aria-label="Soft grey photo of a technician's gloved hands crafting a dental restoration"></div>
      <div class="brand-name brand-name--main">Copper Meadow<br>Dental Lab</div>
      <p class="services-text">We provide fixed restorations (Full-Contour Solid Zirconia, KRT o.lumo, Dune Prime, Full Cast, PFM, Temporary Crowns, Diagnostic Wax-Ups and Study Models), implant restorations (Single and Multi Tooth Restorations, Zirconia Prosthesis, Full Arch Hybrid Prosthesis), and removable restorations (Dentures and Partials, PolyBend, Kernalite).</p>
      <div class="brand-name brand-name--small">Copper Meadow<br>Dental Lab</div>
      <div class="contact-block">
        <div class="contact-name">Copper Meadow Dental Lab</div>
        <div>4126 Orchard Ln, Suite 310, Annandale, VA 22003</div>
        <div class="gap"></div>
        <div>Office number: 703-555-0142</div>
        <div>Fax number: 703-555-0143</div>
        <div class="gap"></div>
        <div>email: info@cmdentalworks.example</div>
        <div class="web">www.cmdentalworks.example</div>
      </div>
    </section>

    <section class="panel panel--front">
      <div class="front-photo" role="img" aria-label="Blue-toned photo of gloved hands holding dental tools over a crown model"></div>
      <p class="tagline">Restore and enhance the natural beauty of the patients' smiles!</p>
      <h1 class="headline">SMILES</h1>
      <p class="front-web">WWW.CMDENTALWORKS.EXAMPLE</p>
    </section>
  </div>
</body>
</html>
```